Moss Pebble Cleaning Tablets needs 4 x labels

We're about to launch a very exciting cleaning product to market and need your help to brand the 4 x bottles. www.mosspebble.com.au will change the way people buy and use household cleaning products whilst significantly reducing the impact on the earth.

The tablets are dropped into the long life recycled plastic bottle, you simply add water, wait for the tab to dissolve and begin cleaning.

Target Market(s)

Women aged between 30 - 65, care for the environment, want to use less plastic, are early adopters and like to try new things. Care about a clean home and using less chemicals. Want less packaging, less plastic, less carbon emissions.

Industry/Entity Type

House Cleaning

Font styles to use
Sans Serif

Requirements
Must have
• Each label must have an obvious colour differentiator and each label must be identical in it's dimensions and information. Should look uniform when all 4 bottles are aligned in the cupboard. Limited / no images apart from logo.
Nice to have
• Simple, clear, bold, striking. Limited / no pictures. Clean lines with lots of space.
Should not have
• Crisp Pane Label must have a strip of blue (hex BAE1FF).
Grit Buster Kitchen Cleaner must have a strip of colour (FFD6F3)
The Fizz Bathroom cleaner must have a colour strip hex # FFFFBA
The Allround Multip Purpose must have a strip of colour Hex #BAFFC9

```html
<!DOCTYPE html>
<html lang="en">
<head>
<meta charset="utf-8">
<title>Moss Pebble Cleaning Tablets – Bottle Labels</title>
<link rel="stylesheet" href="https://fonts.googleapis.com/css2?family=Bebas+Neue&family=Oswald:wght@400;500&display=swap">
<style>
  :root {
    --page: #ffffff;
    --amber: #8a4a1c;
    --amber-deep: #5e2f10;
    --ink-light: #fbf6ef;
    --brand-ink: #123a4f;
    --multi: #baffc9;
    --bath: #ffffba;
    --kitchen: #ffd6f3;
    --window: #bae1ff;
  }
  html, body {
    margin: 0;
    padding: 0;
    width: 1200px;
    height: 848px;
    overflow: hidden;
    background: var(--page);
  }
  .label-set {
    position: relative;
    width: 1200px;
    height: 848px;
    display: flex;
    justify-content: center;
    align-items: center;
    gap: 34px;
  }
  .label {
    --accent: var(--multi);
    width: 216px;
    height: 430px;
    border-radius: 18px;
    background: linear-gradient(180deg, var(--amber) 0%, #9a5420 45%, var(--amber-deep) 100%);
    display: flex;
    flex-direction: column;
    align-items: center;
    box-sizing: border-box;
    padding-top: 40px;
    color: var(--ink-light);
    font-family: "Bebas Neue", sans-serif;
  }
  .label--bathroom { --accent: var(--bath); }
  .label--kitchen { --accent: var(--kitchen); }
  .label--window { --accent: var(--window); }

  .brand {
    display: flex;
    flex-direction: column;
    align-items: center;
    gap: 6px;
  }
  .brand__dot {
    width: 66px;
    height: 66px;
    border-radius: 50%;
    background: var(--accent);
  }
  .brand__name {
    font-size: 17px;
    letter-spacing: 1px;
    color: var(--accent);
  }
  .product-name {
    margin: 22px 0 0;
    font-weight: 400;
    font-size: 27px;
    line-height: 33px;
    text-align: center;
    letter-spacing: 0.2px;
    color: var(--ink-light);
  }
  .strip {
    width: 70px;
    height: 2px;
    background: var(--accent);
    margin: 18px 0;
  }
  .tagline {
    margin: 0;
    font-size: 17px;
    line-height: 25px;
    text-align: center;
    color: var(--accent);
  }
  .volume {
    margin: 0;
    font-family: "Oswald", sans-serif;
    font-size: 13px;
    color: var(--ink-light);
  }
  .origin {
    margin: 10px 0 0;
    font-size: 10px;
    letter-spacing: 0.3px;
    color: var(--accent);
  }
</style>
</head>
<body>
<main class="label-set">

  <section class="label label--multi">
    <div class="brand">
      <span class="brand__dot"></span>
      <span class="brand__name">Moss Pebble</span>
    </div>
    <h2 class="product-name">The Allround Multi<br>Purpose Cleaner</h2>
    <span class="strip"></span>
    <p class="tagline">One Bottle · One Tab ·<br>Dissolve · Clean · Repeat ·</p>
    <span class="strip"></span>
    <p class="volume">500 мл</p>
    <p class="origin">Torquay · Australia</p>
  </section>

  <section class="label label--bathroom">
    <div class="brand">
      <span class="brand__dot"></span>
      <span class="brand__name">Moss Pebble</span>
    </div>
    <h2 class="product-name">The Fizz<br>Bathroom Cleaner</h2>
    <span class="strip"></span>
    <p class="tagline">One Bottle · One Tab ·<br>Dissolve · Clean · Repeat ·</p>
    <span class="strip"></span>
    <p class="volume">500 мл</p>
    <p class="origin">Torquay · Australia</p>
  </section>

  <section class="label label--kitchen">
    <div class="brand">
      <span class="brand__dot"></span>
      <span class="brand__name">Moss Pebble</span>
    </div>
    <h2 class="product-name">Grit Buster<br>Kitchen Cleaner</h2>
    <span class="strip"></span>
    <p class="tagline">One Bottle · One Tab ·<br>Dissolve · Clean · Repeat ·</p>
    <span class="strip"></span>
    <p class="volume">500 мл</p>
    <p class="origin">Torquay · Australia</p>
  </section>

  <section class="label label--window">
    <div class="brand">
      <span class="brand__dot"></span>
      <span class="brand__name">Moss Pebble</span>
    </div>
    <h2 class="product-name">Crisp Pane Window<br>Cleaner</h2>
    <span class="strip"></span>
    <p class="tagline">One Bottle · One Tab ·<br>Dissolve · Clean · Repeat ·</p>
    <span class="strip"></span>
    <p class="volume">500 мл</p>
    <p class="origin">Torquay · Australia</p>
  </section>

</main>
</body>
</html>
```